Wendy Marsh Copywriter Website

I am starting a new business as a freelance copywriter. Trying to set up the website for my business is proving to be too technical for me. I would like a simple, clean website using primarily black and white. I have attached the logo I would like used. I would like the menu icons to be Home, Services, Portfolio, Blog, Contact. I would like my mobile phone number (0412 583 906) and email address (wendy.marsh.copywriter@mailbox-example.com) used in the header of the site. I need the site to be easily manageable and inter-changeable for me to be able to move things around and add images, etc with ease.

I would like the home page to be a static page with space for an image of myself somewhere (I haven't had this taken as yet), an area to put a bit about myself and my business, and also somewhere to include social media icons/links. Again, I would like the whole website and home page to be easily managed so that I can add/delete things with ease.

I would like the image of the typewriter used in the website somewhere also please.

Font styles to use
Sans Serif
Script

Colors
fdf0f6

Requirements
Must have
• The logo provided
• Ability to change page contents easily
• Ability to add social media icons as needed
Nice to have
• Use of the typewriter image
Should not have
• Complicated pages that are not easily editable

```html
<!DOCTYPE html>
<html lang="en">
<head>
<meta charset="utf-8">
<title>Wendy Marsh Copywriter</title>
<link href="https://fonts.googleapis.com/css2?family=Lato:wght@400;700&family=Mr+Dafoe&display=swap" rel="stylesheet">
<style>
:root{
  --ink:#2b2b2b;
  --text:#3a3a3a;
  --pink:#f6e8e9;
  --pink-soft:#f3dede;
  --pink-line:#f0cdd3;
  --pink-accent:#e9b7c0;
  --dot:#c4c4c4;
  --white:#ffffff;
  --script:"Mr Dafoe", cursive;
  --sans:"Lato", sans-serif;
}
*{margin:0;padding:0;box-sizing:border-box}
html,body{width:797px;height:1200px;overflow:hidden}
body{position:relative;background:var(--white);font-family:var(--sans);color:var(--text)}
.ruled{background-image:repeating-linear-gradient(to bottom,transparent 0 17px,var(--pink-line) 17px 18px)}
.binding{position:absolute;top:0;left:0;width:797px;height:18px;
  background:radial-gradient(circle at 5px 9px,var(--dot) 4.5px,transparent 5px) 0 0/23.7px 18px repeat-x}
.site-header{position:absolute;top:18px;left:0;width:797px;height:64px;border-bottom:1px solid var(--pink-line)}
.logo{position:absolute;left:110px;top:22px;display:flex;align-items:center;gap:8px;
  font:400 17px/1 var(--sans);color:var(--ink);letter-spacing:.5px}
.logo-mark{width:10px;height:10px;border-radius:50%;background:var(--pink-accent)}
.contact-line{position:absolute;left:422px;top:10px;font-size:9.5px;display:flex;gap:14px;color:var(--ink)}
.contact-line span{display:flex;align-items:center;gap:4px}
.main-nav{position:absolute;left:402px;top:34px;display:flex;gap:27px;font-size:11.5px;color:var(--ink)}
.main-nav .active{font-weight:700}
.hero{position:absolute;top:82px;left:0;width:797px;height:348px}
.hero-welcome{position:absolute;left:126px;top:72px;font:400 36px/1 var(--script);color:var(--pink-accent)}
.hero-name{position:absolute;left:126px;top:108px;font:400 56px/1 var(--script);color:var(--ink)}
.hero-text{position:absolute;left:130px;top:173px;font-size:10px;line-height:18px;width:280px}
.btn{position:absolute;display:flex;align-items:center;justify-content:center;border-radius:20px;
  font:700 11.5px/1 var(--sans);color:var(--ink);box-shadow:0 1px 3px rgba(0,0,0,.12)}
.btn-hero{left:128px;top:220px;width:125px;height:36px;background:var(--pink-soft)}
.hero-photo{position:absolute;left:455px;top:18px;width:195px;height:265px;
  background:linear-gradient(180deg,#ececec 0 33%,#2a2a2a 33% 100%);border-radius:4px}
.about{position:absolute;top:430px;left:0;width:797px;height:400px;background-color:var(--pink);
  background-image:repeating-linear-gradient(to bottom,transparent 0 17px,#efd9dc 17px 18px);border-top:2px solid #eee}
.about-photo-ring{position:absolute;left:114px;top:44px;width:252px;height:252px;border-radius:50%;
  background:#fbf5f5;box-shadow:0 2px 6px rgba(0,0,0,.1)}
.about-photo{position:absolute;left:12px;top:12px;width:228px;height:228px;border-radius:50%;
  background:radial-gradient(circle at 50% 40%,#9a9a9a,#6d7a8a)}
.section-title{position:absolute;font:400 36px/1 var(--script);color:var(--ink)}
.about .section-title{left:390px;top:58px}
.about-text{position:absolute;left:393px;top:106px;width:280px;font-size:9.6px;line-height:16.8px}
.btn-about{left:390px;top:223px;width:124px;height:35px;background:var(--white)}
.curve{position:absolute;top:766px;left:0;width:797px;height:64px}
.services{position:absolute;top:826px;left:0;width:797px;height:290px}
.services .section-title{left:132px;top:4px}
.services-text{position:absolute;left:139px;top:51px;width:280px;font-size:9.6px;line-height:16.8px}
.services-list{position:absolute;left:144px;top:115px;list-style:none;font-size:10.4px}
.services-list li{display:flex;align-items:center;gap:5px;height:22.4px}
.services-art{position:absolute;left:445px;top:6px;width:245px;height:235px;border-radius:50%;
  background:radial-gradient(circle,#e6e6e6 0 55%,#f6f6f6 56%,transparent 72%)}
.site-footer{position:absolute;top:1116px;left:0;width:797px;height:84px;background:var(--pink);border-top:2px solid #eee}
.footer-nav{position:absolute;left:130px;top:24px;display:flex;gap:26px;font-size:11px;color:var(--ink)}
.copyright{position:absolute;left:130px;top:44px;font-size:8px;color:#555}
.social{position:absolute;left:564px;top:22px;display:flex;gap:5px}
.social span{width:25px;height:25px;border:1.5px solid var(--ink);border-radius:50%}
</style>
</head>
<body>
<div class="binding"></div>

<header class="site-header">
  <div class="logo"><span class="logo-mark"></span>Wendy Marsh Copywriter</div>
  <div class="contact-line">
    <span><svg width="10" height="8" viewBox="0 0 10 8"><rect x=".5" y=".5" width="9" height="7" fill="none" stroke="#2b2b2b"/><path d="M.5 .5 5 4.5 9.5 .5" fill="none" stroke="#2b2b2b"/></svg>wendy.marsh.copywriter@mailbox-example.com</span>
    <span><svg width="9" height="9" viewBox="0 0 10 10"><path d="M2 1l2 2-1 1.5c.8 1.4 1.7 2.3 3 3L7.5 6l2 2-1.5 1.5C4.5 9 1 5.5.5 2z" fill="none" stroke="#2b2b2b"/></svg>(0412 583 906)</span>
  </div>
  <nav class="main-nav"><span class="active">Home</span><span>Services</span><span>Portfolio</span><span>Blog</span><span>Contact</span></nav>
</header>

<section class="hero ruled">
  <p class="hero-welcome">Welcome to</p>
  <h1 class="hero-name">wendy marsh</h1>
  <p class="hero-text">Lorem ipsum dolor sit amet consectetuer adipiscing elit Nam cursus Morbi ut mi Nullam enim leo egestas</p>
  <a class="btn btn-hero">Contact Me</a>
  <div class="hero-photo" role="img" aria-label="Photo of a vintage black typewriter with a sheet of paper"></div>
</section>

<section class="about">
  <div class="about-photo-ring"><div class="about-photo" role="img" aria-label="Portrait photo of the copywriter"></div></div>
  <h2 class="section-title">About me</h2>
  <p class="about-text">Lorem ipsum dolor sit amet consectetuer adipiscing elit Nam cursus Morbi ut mi Nullam enim leo egestas<br>Ael lacus vitae felis vestibulum volutpat Etiam est nunc venenatis in tristique eu imperdiet ac nisl Cum sociis natoque penatibus et magnis dis parturient montes nascetur ridiculus mus In iaculis facilisis massa Etiam eu urna Sed porta</p>
  <a class="btn btn-about">Read More</a>
</section>

<svg class="curve" viewBox="0 0 797 64" preserveAspectRatio="none"><path d="M0 64 Q398 -40 797 64 Z" fill="#fff"/></svg>

<section class="services ruled">
  <h2 class="section-title">What i do</h2>
  <p class="services-text">Ael lacus vitae felis vestibulum volutpat Etiam est nunc venenatis in tristique eu imperdiet ac nisl Cum sociis natoque penatibus et magnis dis parturient montes nascetur</p>
  <ul class="services-list">
    <li><svg width="10" height="10" viewBox="0 0 10 10"><circle cx="5" cy="5" r="5" fill="#f0c4cb"/><path d="M2.8 5.2 4.4 6.7 7.3 3.6" stroke="#fff" stroke-width="1.3" fill="none"/></svg>Class aptent taciti sociosqu</li>
    <li><svg width="10" height="10" viewBox="0 0 10 10"><circle cx="5" cy="5" r="5" fill="#f0c4cb"/><path d="M2.8 5.2 4.4 6.7 7.3 3.6" stroke="#fff" stroke-width="1.3" fill="none"/></svg>Ad litora torquent per conubia</li>
    <li><svg width="10" height="10" viewBox="0 0 10 10"><circle cx="5" cy="5" r="5" fill="#f0c4cb"/><path d="M2.8 5.2 4.4 6.7 7.3 3.6" stroke="#fff" stroke-width="1.3" fill="none"/></svg>Nostra per inceptos</li>
    <li><svg width="10" height="10" viewBox="0 0 10 10"><circle cx="5" cy="5" r="5" fill="#f0c4cb"/><path d="M2.8 5.2 4.4 6.7 7.3 3.6" stroke="#fff" stroke-width="1.3" fill="none"/></svg>Hymenaeos Proin nulla arcu</li>
  </ul>
  <div class="services-art" role="img" aria-label="Line illustration of a hand typing on a typewriter"></div>
</section>

<footer class="site-footer">
  <nav class="footer-nav"><span>Home</span><span>Services</span><span>Portfolio</span><span>Blog</span><span>Contact</span></nav>
  <p class="copyright">© 2018 Company Name&nbsp; All right reserved</p>
  <div class="social">
    <span aria-label="Social link 1"></span><span aria-label="Social link 2"></span><span aria-label="Social link 3"></span><span aria-label="Social link 4"></span>
  </div>
</footer>
</body>
</html>
```